Copperfield Roofing Co. business card design

I am a Roofing contractor in Texas. The name of my company is Copperfield Roofing Co. I also offer a few other services (Christmas light installation, gutters, fencing, pressure washing). However my main gig is roofing. Storm restoration and knowledge of the insurance claim process is my specialty.

My colors are black, red and white. I’d like something pretty simple and clean. Modern looking but with a splash of this red tartan pattern.

I have another version of my logo being edited at the moment where the little top part of the F in roofing that’s currently tartan will be changed to just solid red to make it more visible. So if that’s something you can change in your mock up great. But I can provide the full version once the contest is complete

Target Market(s)

Homeowners

Industry/Entity Type

Roofing

Contact Information for Business Card

Derek Pruitt. 682-555-0193. www.copperfield roofing.co Derek@copperfieldroofing.co

Colors
EB3D1F
EC4F4E
F09395
F8D3D4
FCEDEE

Requirements
Nice to have
• Maybe instead of a business address. I could say serving all DFW Texas or something like that. And maybe add a line somewhere saying deductible assistance? Just a thought

```html
<!DOCTYPE html>
<html lang="en">
<head>
<meta charset="utf-8">
<title>Copperfield Roofing Co. – Business Card</title>
<link rel="stylesheet" href="https://fonts.googleapis.com/css2?family=Audiowide&family=Open+Sans:wght@400;600&display=swap">
<style>
  :root {
    --canvas: #d4d5d7;
    --black: #000000;
    --red: #e0201f;
    --red-deep: #a8161a;
    --red-dark: #6b0e10;
    --white: #ffffff;
  }
  * { margin: 0; padding: 0; box-sizing: border-box; }
  html, body { width: 900px; height: 1200px; overflow: hidden; background: var(--canvas); }
  .stage { position: relative; width: 900px; height: 1200px; }

  .card {
    position: absolute; left: 122px; width: 657px; height: 375px;
    border-radius: 11px; overflow: hidden;
  }
  .card--front { top: 204px; }
  .card--back { top: 621px; background: var(--black); }

  .tartan-fill {
    position: absolute; inset: 0;
    background: linear-gradient(160deg, var(--red-deep) 0%, var(--red) 42%, var(--red-deep) 72%, var(--red-dark) 100%);
  }
  .tartan-strip {
    position: absolute; left: 0; right: 0; bottom: 0; height: 14px;
    background: linear-gradient(90deg, var(--red-deep) 0%, var(--red) 45%, var(--red-deep) 75%, var(--red-dark) 100%);
  }

  .brand { position: absolute; left: 0; right: 0; text-align: center; }
  .brand__mark { display: block; margin: 0 auto; }
  .brand__name {
    font-family: 'Audiowide', sans-serif; color: var(--white);
    text-transform: uppercase; line-height: 1.05;
  }
  .brand__name span { display: block; }
  .card--front .brand { top: 72px; }
  .card--front .brand__name { margin-top: 18px; font-size: 38px; }
  .card--front .brand__name span { font-size: 28px; margin-top: 2px; }
  .card--back .brand { top: 49px; }
  .card--back .brand__name { margin-top: 12px; font-size: 27px; }
  .card--back .brand__name span { font-size: 18px; margin-top: 1px; }

  .person {
    position: absolute; right: 353px; top: 272px; text-align: right;
  }
  .person__name {
    font-family: 'Audiowide', sans-serif; font-size: 25px; line-height: 1;
    text-transform: uppercase; color: var(--white);
  }
  .person__first { color: var(--red); }
  .person__role {
    margin-top: 8px; font-family: 'Open Sans', sans-serif; font-size: 16px; color: var(--white);
  }
  .person__role em { font-style: normal; color: var(--red); }

  .divider {
    position: absolute; left: 328px; top: 263px; width: 1px; height: 71px; background: var(--white);
  }

  .contacts {
    position: absolute; left: 350px; top: 258px; list-style: none;
    font-family: 'Open Sans', sans-serif; font-size: 16px; letter-spacing: 0.5px; color: var(--white);
  }
  .contacts li { display: flex; align-items: center; height: 26px; gap: 6px; }
  .contacts .phone { letter-spacing: 2.5px; }
  .contacts svg { width: 15px; height: 15px; flex: none; }
</style>
</head>
<body>
<main class="stage">

  <section class="card card--front">
    <div class="tartan-fill" role="img" aria-label="Red, black and white tartan pattern"></div>
    <div class="brand">
      <svg class="brand__mark" width="150" height="150" viewBox="0 0 150 150" aria-hidden="true">
        <circle cx="75" cy="75" r="72" fill="var(--red)" stroke="var(--white)" stroke-width="5"/>
      </svg>
      <p class="brand__name">Copperfield<span>Roofing Co.</span></p>
    </div>
  </section>

  <section class="card card--back">
    <div class="brand">
      <svg class="brand__mark" width="108" height="108" viewBox="0 0 108 108" aria-hidden="true">
        <circle cx="54" cy="54" r="51" fill="var(--red)" stroke="var(--white)" stroke-width="4"/>
      </svg>
      <p class="brand__name">Copperfield<span>Roofing Co.</span></p>
    </div>

    <div class="person">
      <p class="person__name"><span class="person__first">Derek</span> Pruitt</p>
      <p class="person__role">Roofing contractor in <em>Texas</em></p>
    </div>

    <div class="divider"></div>

    <ul class="contacts">
      <li class="phone">
        <svg viewBox="0 0 24 24" aria-hidden="true"><path fill="var(--red)" d="M6.6 10.8a15.1 15.1 0 0 0 6.6 6.6l2.2-2.2a1 1 0 0 1 1-.25 11.4 11.4 0 0 0 3.6.57 1 1 0 0 1 1 1V20a1 1 0 0 1-1 1A17 17 0 0 1 3 4a1 1 0 0 1 1-1h3.5a1 1 0 0 1 1 1c0 1.25.2 2.45.57 3.57a1 1 0 0 1-.25 1z"/></svg>
        682-555-0193
      </li>
      <li>
        <svg viewBox="0 0 24 24" aria-hidden="true"><rect x="2" y="5" width="20" height="14" fill="var(--red)"/><path d="M2 5l10 8 10-8" fill="none" stroke="var(--black)" stroke-width="1.6"/></svg>
        Derek@copperfieldroofing.co
      </li>
      <li>
        <svg viewBox="0 0 24 24" aria-hidden="true"><g fill="none" stroke="var(--red)" stroke-width="1.8"><circle cx="12" cy="12" r="9"/><ellipse cx="12" cy="12" rx="4" ry="9"/><path d="M3 12h18M5 7h14M5 17h14"/></g></svg>
        www.copperfieldroofing.co
      </li>
    </ul>

    <div class="tartan-strip" role="img" aria-label="Strip of red, black and white tartan pattern"></div>
  </section>

</main>
</body>
</html>
```